Supplement Company Needs a Protein Powder Pouch Design

We are looking for a modern and fresh design for our 500g pouches of protein powder as our current design is not eye catching or exciting enough.

This new design will be printed on both sides of a 178mm x 280mm x 101mm pouch.

We have 4 flavours. These are Banana Ice Cream, Chocolate Deluxe, Strawberries & Cream and Vanilla Ice Cream.
Updates

Need extra days to review

Industry/Entity Type

Supplement

Requirements
Must have
• Attractive and eye catching front and space for all the nutritional information and ingredients on the back.

Must clearly state 'food supplement' somewhere on the front of the pouch.
Nice to have
• Our logo is attached.
Should not have
• No health claims as these are not allowed in the UK

```html
<!DOCTYPE html>
<html lang="en">
<head>
<meta charset="utf-8">
<title>KIVO Supplements – Protein Powder Chocolate Deluxe Pouch</title>
<link rel="stylesheet" href="https://fonts.googleapis.com/css2?family=Montserrat:wght@100;200;400;500;800;900&display=swap">
<style>
  :root {
    --pouch-black: #000000;
    --cocoa: #9a5a33;
    --cocoa-dark: #8a4f2c;
    --leaf-green: #9bc644;
    --white: #ffffff;
    --choc-light: #a9683f;
    --choc-deep: #5b3018;
  }
  * { margin: 0; padding: 0; box-sizing: border-box; }
  html, body { width: 772px; height: 1200px; overflow: hidden; background: var(--white); }
  body { font-family: "Montserrat", sans-serif; color: var(--white); }

  .pouch-front { position: relative; width: 772px; height: 1200px; background: var(--pouch-black); overflow: hidden; }

  .texture-block { position: absolute; background: linear-gradient(135deg, var(--cocoa) 0%, var(--cocoa-dark) 100%); }
  .texture-block--top-left { left: 0; top: 0; width: 254px; height: 323px; }
  .texture-block--top-right { left: 526px; top: 0; width: 246px; height: 323px; }
  .texture-block--band { left: 0; top: 694px; width: 772px; height: 56px; }
  .texture-block--footer { left: 0; top: 1048px; width: 772px; height: 152px; }

  .accent-rule { position: absolute; background: var(--leaf-green); height: 9px; }
  .accent-rule--top-left { left: 0; top: 323px; width: 254px; }
  .accent-rule--top-right { left: 526px; top: 323px; width: 246px; }
  .accent-rule--under-brand { left: 254px; top: 422px; width: 272px; }
  .accent-rule--footer { left: 0; top: 1039px; width: 772px; }

  .brand { position: absolute; left: 254px; top: 285px; width: 272px; text-align: center; font-weight: 800; color: var(--white); }
  .brand__name { display: block; font-size: 68px; line-height: 1; letter-spacing: -1px; }
  .brand__sub { display: block; font-size: 11px; letter-spacing: 9.5px; margin-top: 6px; padding-left: 9px; }

  .product-title { position: absolute; left: 187px; top: 520px; font-weight: 900; color: var(--cocoa); font-size: 77px; line-height: 67px; letter-spacing: 3.5px; white-space: nowrap; }

  .supplement-label { position: absolute; left: 0; top: 694px; width: 772px; height: 56px; display: flex; align-items: center; justify-content: center; font-weight: 800; font-size: 34px; letter-spacing: 5.8px; padding-left: 8px; white-space: nowrap; }

  .flavour-visual { position: absolute; left: 347px; top: 793px; width: 76px; height: 57px; }

  .flavour { position: absolute; left: 0; width: 772px; text-align: center; font-weight: 100; white-space: nowrap; }
  .flavour__name { top: 878px; font-size: 61px; letter-spacing: 7px; padding-left: 7px; }
  .flavour__desc { top: 948px; font-size: 44px; letter-spacing: 4px; padding-left: 4px; }

  .usage-info { position: absolute; left: 86px; top: 1066px; font-size: 11.8px; line-height: 13.4px; font-weight: 400; white-space: nowrap; }
  .usage-info p + p { margin-top: 8px; }

  .net-weight { position: absolute; left: 620px; top: 1083px; font-size: 27px; font-weight: 500; letter-spacing: 1px; }
</style>
</head>
<body>
<main class="pouch-front">
  <div class="texture-block texture-block--top-left" role="img" aria-label="Cocoa brown chevron pattern"></div>
  <div class="texture-block texture-block--top-right" role="img" aria-label="Cocoa brown chevron pattern"></div>
  <div class="accent-rule accent-rule--top-left"></div>
  <div class="accent-rule accent-rule--top-right"></div>

  <div class="brand">
    <span class="brand__name">KIVO</span>
    <span class="brand__sub">SUPPLEMENTS</span>
  </div>
  <div class="accent-rule accent-rule--under-brand"></div>

  <h1 class="product-title">PROTEIN<br>POWDER</h1>

  <div class="texture-block texture-block--band" role="img" aria-label="Cocoa brown chevron pattern"></div>
  <p class="supplement-label">FOOD SUPPLEMENT</p>

  <svg class="flavour-visual" viewBox="0 0 76 57" role="img" aria-label="Pieces of milk chocolate">
    <defs>
      <radialGradient id="chocTone" cx="50%" cy="45%" r="55%">
        <stop offset="0" stop-color="#a9683f"/>
        <stop offset="1" stop-color="#5b3018"/>
      </radialGradient>
    </defs>
    <ellipse cx="38" cy="29" rx="36" ry="25" fill="url(#chocTone)"/>
  </svg>

  <h2 class="flavour flavour__name">CHOCOLATE</h2>
  <p class="flavour flavour__desc">DELUXE FLAVOUR</p>

  <div class="accent-rule accent-rule--footer"></div>
  <div class="texture-block texture-block--footer" role="img" aria-label="Cocoa brown chevron pattern"></div>

  <div class="usage-info">
    <p>SUGGESTED USE: We recommend using one to two servings of 30g per day. One<br>serving is one level scoop (a scoop is inside this pouch). Mix one level scoop with<br>at least 200ml of cold water. Do not exceed recommended daily dose.</p>
    <p>STORAGE INFORMATION: Store in a cool and dry place. Reseal this pouch after<br>each use. Keep out of sight and reach of children.</p>
  </div>
  <p class="net-weight">500 G</p>
</main>
</body>
</html>
```